Business Card design for Founder and CEO of new shoe company

I am looking for a business card design for my new shoe company called Strido.

I am launching the company this April. Strido shoes offers slip-on athletic and casual style shoes for men and women. The unique selling point of the brand is that all of our shoe exist without shoelaces. I have included a link to the website to offer additional information about the company, see product images, and gain inspiration for the design. You can use the store owner password "Strido" to access the website.

www.Strido-shop.example

Thanks,
Dean Porlow

Target Market(s)

Active Men and Women ages 16-45

Industry/Entity Type

Business

Contact Information for Business Card

Dean Porlow
Founder and CEO
www.Strido-shop.example
deanporlow@Strido-shop.example
888-730-1964 / 888-7STRIDO
Strido, LLC
2384 N Tarrow St
Chicago, IL 60614

Requirements
Must have
• Be able to quickly and easily tell that Strido is a shoe company from the business card

```html
<!DOCTYPE html>
<html lang="en">
<head>
<meta charset="utf-8">
<title>Strido business card</title>
<link rel="stylesheet" href="https://fonts.googleapis.com/css2?family=Open+Sans:wght@400;600;700&display=swap">
<style>
  :root {
    --stage: #2b2b2b;
    --card-black: #050505;
    --card-white: #ffffff;
    --ink: #111111;
    --ink-soft: #222222;
    --photo-light: #b9b6b1;
    --photo-dark: #8f8c87;
  }
  * { box-sizing: border-box; margin: 0; padding: 0; }
  html, body { width: 1200px; height: 900px; overflow: hidden; }
  body {
    background: var(--stage);
    font-family: "Open Sans", Arial, sans-serif;
    position: relative;
  }
  .card {
    position: absolute;
    width: 600px;
    height: 343px;
    border-radius: 22px;
    overflow: hidden;
    box-shadow: 0 14px 30px rgba(0,0,0,0.45);
  }
  .card-back {
    left: 300px; top: 70px;
    background: var(--card-black);
    display: flex; align-items: center; justify-content: center;
  }
  .brand-name {
    font-weight: 400;
    color: var(--card-white);
    font-size: 64px;
    letter-spacing: 1px;
  }
  .card-front {
    left: 300px; top: 470px;
    background: var(--card-white);
  }
  .front-art { position: absolute; inset: 0; }
  .front-brand {
    position: absolute; left: 34px; top: 34px;
    font-size: 40px; font-weight: 400; color: var(--ink);
  }
  .contact {
    position: absolute; left: 40px; top: 160px;
    color: var(--ink-soft);
  }
  .contact-name {
    font-size: 27px; font-weight: 700; letter-spacing: 0.5px; line-height: 1.1; color: var(--ink);
  }
  .contact-title { font-size: 15px; margin-bottom: 6px; }
  .contact-line {
    display: flex; align-items: center; gap: 8px;
    font-size: 14px; line-height: 21px;
  }
  .contact-line svg { width: 12px; height: 12px; flex: none; }
  .contact-address { font-size: 14px; line-height: 20px; margin-top: 10px; }
</style>
</head>
<body>

<section class="card card-back" aria-label="Card back">
  <span class="brand-name">Strido</span>
</section>

<section class="card card-front" aria-label="Card front">
  <svg class="front-art" viewBox="0 0 600 343" preserveAspectRatio="none">
    <defs>
      <linearGradient id="concrete" x1="0" y1="0" x2="1" y2="1">
        <stop offset="0" stop-color="var(--photo-light)"/>
        <stop offset="1" stop-color="var(--photo-dark)"/>
      </linearGradient>
    </defs>
    <path role="img" aria-label="Photo of colourful slip-on sneakers arranged in a circle on concrete"
          d="M190 0 H600 V343 H430 C400 250 330 210 280 170 C230 130 210 60 190 0 Z"
          fill="url(#concrete)"/>
    <path d="M190 0 C210 60 230 130 280 170 C330 210 400 250 430 343"
          fill="none" stroke="var(--ink)" stroke-width="4"/>
  </svg>

  <span class="front-brand">Strido</span>

  <div class="contact">
    <p class="contact-name">DEAN PORLOW</p>
    <p class="contact-title">Founder and CEO</p>
    <p class="contact-line">
      <svg viewBox="0 0 24 24"><path fill="currentColor" d="M6.6 10.8a15 15 0 0 0 6.6 6.6l2.2-2.2c.3-.3.7-.4 1-.2 1.1.4 2.3.6 3.6.6.6 0 1 .4 1 1V20c0 .6-.4 1-1 1A17 17 0 0 1 3 4c0-.6.4-1 1-1h3.5c.6 0 1 .4 1 1 0 1.3.2 2.5.6 3.6.1.3 0 .7-.2 1z"/></svg>
      888-730-1964 / 888-7STRIDO
    </p>
    <p class="contact-line">
      <svg viewBox="0 0 24 24"><rect x="2" y="5" width="20" height="14" rx="1.5" fill="none" stroke="currentColor" stroke-width="2"/><path d="M2 6l10 7 10-7" fill="none" stroke="currentColor" stroke-width="2"/></svg>
      deanporlow@Strido-shop.example
    </p>
    <p class="contact-line">
      <svg viewBox="0 0 24 24"><circle cx="12" cy="12" r="10" fill="none" stroke="currentColor" stroke-width="2"/><ellipse cx="12" cy="12" rx="4.5" ry="10" fill="none" stroke="currentColor" stroke-width="2"/><path d="M2 12h20" stroke="currentColor" stroke-width="2"/></svg>
      www.Strido-shop.example
    </p>
    <p class="contact-address">Strido, LLC 2384 N Tarrow St<br>Chicago, IL 60614</p>
  </div>
</section>

</body>
</html>
```